Anesthesia Medical Practice Business Card

We need a business card to hand out to surgeons with my basic information. Something that stands out but is not over the top. The medical community is rather conservative. I'd like them to call me first when flipping through their rolodex of anesthesiologists. I'd like the card to communicate confidence, control, professionalism yet serenity. I don't want the card to be pricey to print.

he logo will be provided as a vector graphic in addition to a complete business card design including the logo

Ravi Pell Okonedo, M.D.
Board Certified Anesthesiologist

(310) 555-0186

rokonedo@mailvane.net

Mailing Address:
48315 Corbel Ave.
Suite 270-4863
Los Angeles, CA 90024

A logo that inegrates my initials perhaps
RO MD
My initials are RO and MD as in Medical Doctor

or
perhaps a physician in surgical mask and cap caring for a patient

Target Market(s)

Surgeons who need anesthesia services

Industry/Entity Type

Medical

Requirements
Must have
• the logo will be provided as a vector graphic in addition to a complete business card design including the logo

Ravi Pell Okonedo, M.D.

(310) 555-0186

rokonedo@mailvane.net

Mailing Address:
48315 Corbel Ave.
Suite 270-4863
Los Angeles, CA 90024

Nice to have
• A logo that inegrates my initials perhaps
RO MD

or

```html
<!DOCTYPE html>
<html lang="en">
<head>
<meta charset="utf-8">
<title>Ravi Pell Okonedo, M.D. — Business Card</title>
<link rel="stylesheet" href="https://fonts.googleapis.com/css2?family=Josefin+Sans:wght@300;400&display=swap">
<style>
  :root {
    --backdrop: #3b322d;
    --card: #ffffff;
    --ink: #1c1c1c;
    --muted: #a9a9a9;
    --shadow: rgba(0, 0, 0, 0.35);
  }
  * { margin: 0; padding: 0; box-sizing: border-box; }
  html, body {
    width: 1200px;
    height: 1000px;
    overflow: hidden;
    background: var(--backdrop);
    font-family: "Josefin Sans", sans-serif;
    color: var(--ink);
  }
  .business-card {
    position: absolute;
    left: 180px;
    top: 260px;
    width: 840px;
    height: 480px;
    background: var(--card);
    box-shadow: 0 14px 30px var(--shadow);
  }
  .identity {
    position: absolute;
    left: 90px;
    top: 160px;
  }
  .identity__name {
    font-weight: 400;
    font-size: 30px;
    letter-spacing: 1.5px;
  }
  .identity__title {
    font-weight: 300;
    font-size: 19px;
    letter-spacing: 1px;
    color: var(--muted);
    margin-top: 4px;
  }
  .contact {
    list-style: none;
    margin-top: 16px;
    padding-left: 10px;
    font-weight: 300;
    font-size: 20px;
    letter-spacing: 1px;
    line-height: 1.45;
  }
  .monogram {
    position: absolute;
    right: 70px;
    top: 95px;
    font-weight: 400;
    font-size: 58px;
    letter-spacing: 3px;
    color: var(--ink);
  }
  .mailing {
    position: absolute;
    right: 60px;
    bottom: 50px;
    text-align: right;
    font-style: normal;
    font-weight: 300;
    font-size: 17px;
    letter-spacing: 1px;
    line-height: 1.35;
  }
</style>
</head>
<body>
  <article class="business-card">
    <div class="monogram">RO MD</div>

    <header class="identity">
      <h1 class="identity__name">Ravi Pell Okonedo, M.D.</h1>
      <p class="identity__title">Board Certified Anesthesiologist</p>
      <ul class="contact">
        <li>p: (310) 555-0186</li>
        <li>e: rokonedo@mailvane.net</li>
      </ul>
    </header>

    <address class="mailing">
      Mailing Address:<br>
      48315 Corbel Ave.<br>
      Suite 270-4863<br>
      Los Angeles, CA 90024
    </address>
  </article>
</body>
</html>
```